Business Broker Website

Hi.
I need a new design done for a business broker website. An example of the style of website I like is https://marlowvantage.example/
The menu needs to be :
* Home
* Businesses for Sale
* What we do
* Our people
* Industries
* Blog
* Confidentiality
* Contact
The home page needs to include a section saying 'businesses sold' with each having a photo, heading and short description. It also needs to have a place to show a video which I have attached so you can take a screenshot to put it on the page.
The content on the home page needs to be as follows:
Harbourline Ventures Group are a boutique brokerage business, specializing in the sales and marketing of SME businesses throughout Queensland and, the Northern Territory
who we are
Welcome to Harbourline Ventures Group. Our specialization is in the marketing and acquisition of closely held businesses throughout Queensland and the Northern Territory. We concentrate in SME businesses in the turnovers of approximately $1,000,000 to $10,000,000 +.
The combined business experience and industry knowledge of our principal is unparalleled and fully committed to a “customer first always” approach to doing business.
Our seller’s benefit from a multi-faceted strategic marketing plan, custom prepared for each seller, no two marketing campaigns are the same. This assures maximum exposure to well-qualified Buyers, while strictly maintaining confidentiality.
We have the comprehensive knowledge and resources to help our Buyers identify their perfect business acquisition– perhaps even if that business is not currently listed for sale!
"the whole secret of a successful life is to find out what is one's destiny to do, and then do it." walter pryce
people looking to buy or sell businesses
1 page

```html
<!DOCTYPE html>
<html lang="en">
<head>
<meta charset="utf-8">
<title>Harbourline Ventures Group</title>
<link href="https://fonts.googleapis.com/css2?family=Lato:ital,wght@0,400;0,700;0,900;1,700;1,900&family=Raleway:wght@600;700;800&display=swap" rel="stylesheet">
<style>
:root{
  --purple:#503c87;
  --purple-deep:#45347a;
  --ink:#3c3c3f;
  --dark:#47474b;
  --text:#5f5f66;
  --grey-line:#c9c9cf;
  --white:#ffffff;
  --red:#e3262b;
  --sold:#5d5d63;
}
*{box-sizing:border-box;margin:0;padding:0}
html,body{width:1200px;height:3507px;overflow:hidden;background:var(--white)}
body{position:relative;font-family:"Lato",sans-serif;color:var(--text)}
.abs{position:absolute}

/* header */
.brand{left:135px;top:18px;display:flex;align-items:center;gap:12px}
.brand-dot{width:44px;height:44px;border-radius:50%;background:var(--purple)}
.brand-name{font-family:"Raleway",sans-serif;font-weight:800;font-size:25px;color:var(--purple);white-space:nowrap}
.call{left:596px;top:22px;display:flex;align-items:center;gap:10px;font-family:"Lato",sans-serif;font-weight:700;font-size:21px;color:var(--purple)}
.call svg{width:36px;height:36px}
.login{left:927px;top:15px;width:128px;height:50px;border-radius:25px;background:var(--ink);color:var(--white);font-weight:900;font-size:17px;display:flex;align-items:center;padding-left:30px;gap:12px}
.btn-dot{width:30px;height:30px;border-radius:50%;background:var(--white);display:flex;align-items:center;justify-content:center}
.btn-dot svg{width:14px;height:14px}

/* nav */
.nav{left:0;top:80px;width:1200px;height:54px;background:var(--purple-deep)}
.nav ul{list-style:none;display:flex;position:absolute;left:144px;top:0;height:54px}
.nav li{font-family:"Lato",sans-serif;font-weight:700;font-size:11.5px;color:var(--white);height:54px;display:flex;align-items:center;padding:0 14px}
.nav li.active{background:#3a3a3e;padding:0 20px}

/* hero */
.hero{left:0;top:134px;width:1200px;height:560px;border-radius:0 0 90px 90px;overflow:hidden;background:linear-gradient(120deg,#0c1d4a 0%,#274f8f 40%,#5d86c1 65%,#2a4a8a 100%)}
.hero-title{left:143px;top:124px;width:490px;font-family:"Raleway",sans-serif;font-weight:800;font-size:34px;line-height:41px;color:var(--white);text-shadow:0 2px 4px rgba(0,0,0,.4)}
.play{left:586px;top:494px;width:28px;height:28px}
.form{left:720px;top:184px;width:335px;height:459px;background:var(--white);border-radius:3px;text-align:center}
.form h2{font-family:"Raleway",sans-serif;font-weight:700;font-size:27px;line-height:33px;color:var(--ink);margin-top:34px}
.form h2 span{color:var(--purple)}
.field{position:absolute;left:25px;width:285px;border:1px solid var(--grey-line);font-size:13px;color:var(--text);text-align:left;padding:16px 23px}
.submit{left:104px;top:372px;width:128px;height:50px;border-radius:25px;background:var(--ink);color:var(--white);font-weight:900;font-size:16px;display:flex;align-items:center;padding-left:21px;gap:10px}
.form-swirl{left:20px;top:350px;width:90px;height:90px;border-radius:50%;background:#e6e4ee}

/* who we are */
.who-bg{left:0;top:694px;width:1200px;height:548px;background:linear-gradient(180deg,#ffffff 0%,#f3f2f6 55%,#e4e2ea 100%)}
.who-photo{left:198px;top:780px;width:387px;height:387px;border-radius:50%;background:radial-gradient(circle at 45% 40%,#6b5b97 0%,#3b2f63 60%,#2b2540 100%)}
.ghost{font-family:"Raleway",sans-serif;font-weight:800;color:#e9e8ee;white-space:nowrap}
.who-ghost{left:630px;top:756px;font-size:80px}
.h-section{font-family:"Raleway",sans-serif;font-weight:800;color:var(--purple);white-space:nowrap}
.who-title{left:631px;top:782px;font-size:46px}
.who-text{left:631px;top:858px;width:420px;font-size:13px;line-height:24px;text-align:justify}
.btn{height:52px;border-radius:26px;background:var(--ink);color:var(--white);font-weight:900;font-size:16px;display:flex;align-items:center;gap:10px;padding-left:20px}

/* quote */
.quote{left:0;top:1242px;width:1200px;height:202px;background:linear-gradient(90deg,#4d3a84 0%,#4a3780 60%,#3c3270 100%);text-align:center;color:var(--white)}
.quote p{font-family:"Lato",sans-serif;font-style:italic;font-weight:900;font-size:28px;line-height:38px;margin-top:34px}
.quote cite{display:block;font-style:normal;font-weight:900;font-size:26px;margin-top:22px;letter-spacing:.5px}

/* businesses sold */
.sold-bg{left:0;top:1444px;width:1200px;height:1686px;background:linear-gradient(180deg,#f1f1f5 0%,#ffffff 25%,#eeeef3 55%,#f3f3f6 100%)}
.sold-ghost{left:237px;top:1524px;font-size:80px}
.sold-title{left:0;width:1200px;top:1554px;text-align:center;font-size:46px}
.frame{border:5px solid var(--purple);width:258px;height:256px}
.photo{width:435px;height:340px}
.tag{height:35px;color:var(--white);font-weight:900;font-size:20px;display:flex;align-items:center;justify-content:center;width:87px}
.tag.sale{background:var(--red)}
.tag.sold{background:var(--sold)}
.item-title{font-family:"Lato",sans-serif;font-weight:700;font-size:24px;color:var(--ink);white-space:nowrap}
.item-text{width:414px;font-size:12.5px;line-height:24px;color:var(--text)}

/* footer */
.footer{left:0;top:3130px;width:1200px;height:302px;background:var(--dark);border-radius:90px 90px 0 0}
.foot-brand{left:145px;top:3230px;display:flex;align-items:center;gap:12px}
.foot-brand .brand-dot{background:var(--white)}
.foot-brand .brand-name{color:var(--white)}
.social{top:3318px;width:40px;height:40px;border:1.5px solid var(--white);border-radius:50%}
.foot-h{font-family:"Raleway",sans-serif;font-weight:700;font-size:23px;color:var(--white)}
.foot-t{font-size:13px;color:var(--white);line-height:22px}
.legal{left:0;top:3432px;width:1200px;height:75px;background:var(--purple-deep);color:var(--white);font-size:13px;text-align:center;line-height:75px}
</style>
</head>
<body>

<!-- header -->
<div class="abs brand"><div class="brand-dot"></div><div class="brand-name">Harbourline Ventures Group</div></div>
<div class="abs call">
  <svg viewBox="0 0 36 36"><circle cx="18" cy="18" r="16" fill="none" stroke="#503c87" stroke-width="2"/><path d="M12 10c1-1 2.5-1 3 0l2 3c.5 1 0 2-1 2.5-.5.3-.5 1 0 2l2.5 3c.7.7 1.5.7 2 .2.7-1 2-1.2 2.7-.5l2.3 2.3c.8.8.6 2-.3 2.7-3 2.3-7.5.5-11-3.5S9.5 13 12 10z" fill="#503c87"/></svg>
  CALL US : +1 555 014 2290
</div>
<div class="abs login">LOGIN <span class="btn-dot"><svg viewBox="0 0 14 14"><path d="M4 2l6 5-6 5" fill="none" stroke="#503c87" stroke-width="2.4"/></svg></span></div>

<nav class="abs nav">
  <ul>
    <li class="active">HOME</li><li>BUSINESSES FOR SALE</li><li>WHAT WE DO</li><li>OUR PEOPLE</li><li>INDUSTRIES</li><li>BLOG</li><li>CONFIDENTIALITY</li><li>CONTACT</li>
  </ul>
</nav>

<!-- hero -->
<section class="abs hero" role="img" aria-label="Video still: glass office towers seen from below against a blue sky">
  <h1 class="abs hero-title">Harbourline Ventures Group are a boutique brokerage business, specializing in the sales and marketing of SME businesses throughout Queensland and, the Northern Territory</h1>
  <svg class="abs play" viewBox="0 0 28 28"><circle cx="14" cy="14" r="13" fill="#fff"/><path d="M11 8l9 6-9 6z" fill="#2c3a68"/></svg>
</section>

<form class="abs form">
  <h2>We Will Find You<br><span>The Perfect Company</span><br>To Buy</h2>
  <div class="field" style="top:156px;height:49px">Enter Name</div>
  <div class="field" style="top:212px;height:49px">Enter Email</div>
  <div class="field" style="top:268px;height:80px">Message</div>
  <div class="abs form-swirl"></div>
  <div class="abs submit">SUBMIT <span class="btn-dot"><svg viewBox="0 0 14 14"><path d="M4 2l6 5-6 5" fill="none" stroke="#503c87" stroke-width="2.4"/></svg></span></div>
</form>

<!-- who we are -->
<section class="abs who-bg" role="img" aria-label="Faint background photo of a smiling business team"></section>
<div class="abs who-photo" role="img" aria-label="Photo of colleagues meeting in an office, purple tinted"></div>
<div class="abs ghost who-ghost">WHO WE ARE</div>
<h2 class="abs h-section who-title">Who We Are</h2>
<p class="abs who-text">Welcome to Harbourline Ventures Group. Our specialization is in the marketing and acquisition of closely held businesses throughout Queensland and the Northern Territory. We concentrate in SME businesses in the turnovers of approximately $1,000,000 to $10,000,000 +.The combined business experience and industry knowledge of our principal is unparalleled and fully committed to a “customer first always” approach to doing business.Our seller’s benefit from a multi-faceted strategic marketing plan, custom prepared for each seller, no two marketing campaigns are the same.</p>
<div class="abs btn" style="left:631px;top:1106px;width:160px">READ MORE <span class="btn-dot"><svg viewBox="0 0 14 14"><path d="M4 2l6 5-6 5" fill="none" stroke="#503c87" stroke-width="2.4"/></svg></span></div>

<!-- quote -->
<section class="abs quote">
  <p>"The whole secret of a successful life is to<br>find out what is one's destiny to do, and then do it.</p>
  <cite>- WALTER PRYCE</cite>
</section>

<!-- businesses sold -->
<section class="abs sold-bg" role="img" aria-label="Faint background of glass buildings and office colleagues"></section>
<div class="abs ghost sold-ghost">BUSINESSES SOLD</div>
<h2 class="abs h-section sold-title">Businesses Sold</h2>

<!-- item 1 -->
<div class="abs frame" style="left:82px;top:1834px"></div>
<div class="abs photo" style="left:146px;top:1694px;background:linear-gradient(135deg,#cfd6dc,#8d99a4 55%,#4b5560)" role="img" aria-label="Photo of a businesswoman at a meeting table with colleagues"></div>
<div class="abs tag sale" style="left:478px;top:1712px">SALE</div>
<h3 class="abs item-title" style="left:642px;top:1722px">Nemo enim ipsam voluptatem</h3>
<p class="abs item-text" style="left:642px;top:1772px">Lorem ipsum dolor sit amet, consectetur adipiscing elit, sed do eiusmod tempor incididunt ut labore et dolore magna aliquis ipsum suspendisse ultrices gravida. Risus commodo viverra maecenas accumsan lacus vel facilisis. Lorem ipsum dolor sit amet, consectetur adipiscing elit, sed do eiusmod tempor incididunt ut labore et dolore magna aliquaus ipsum suspendisse ultrices gus coenas accumsan lacus vel facilisis.</p>
<div class="abs btn" style="left:642px;top:1947px;width:160px">READ MORE <span class="btn-dot"><svg viewBox="0 0 14 14"><path d="M4 2l6 5-6 5" fill="none" stroke="#503c87" stroke-width="2.4"/></svg></span></div>

<!-- item 2 -->
<div class="abs frame" style="left:858px;top:2321px"></div>
<div class="abs photo" style="left:620px;top:2181px;background:linear-gradient(135deg,#b9c2c6,#6e7a80 55%,#2f3438)" role="img" aria-label="Photo of a team working on laptops around a long table"></div>
<div class="abs tag sold" style="left:953px;top:2199px">SOLD</div>
<h3 class="abs item-title" style="left:146px;top:2209px">Ut enim ad minima veniauis nostrum</h3>
<p class="abs item-text" style="left:146px;top:2259px">Lorem ipsum dolor sit amet, consectetur adipiscing elit, sed do eiusmod tempor incididunt ut labore et dolore magna aliquis ipsum suspendisse ultrices gravida. Risus commodo viverra maecenas accumsan lacus vel facilisis. Lorem ipsum dolor sit amet, consectetur adipiscing elit, sed do eiusmod tempor incididunt ut labore et dolore magna aliquaus ipsum suspendisse ultrices gus coenas accumsan lacus vel facilisis.</p>
<div class="abs btn" style="left:146px;top:2434px;width:160px">READ MORE <span class="btn-dot"><svg viewBox="0 0 14 14"><path d="M4 2l6 5-6 5" fill="none" stroke="#503c87" stroke-width="2.4"/></svg></span></div>

<!-- item 3 -->
<div class="abs frame" style="left:82px;top:2808px"></div>
<div class="abs photo" style="left:146px;top:2669px;background:linear-gradient(135deg,#c9cfc8,#7d8581 55%,#3a3d44)" role="img" aria-label="Photo of three business people reviewing documents"></div>
<div class="abs tag sale" style="left:478px;top:2687px">SALE</div>
<h3 class="abs item-title" style="left:642px;top:2697px">Nemo enim ipsam voluptatem</h3>
<p class="abs item-text" style="left:642px;top:2747px">Lorem ipsum dolor sit amet, consectetur adipiscing elit, sed do eiusmod tempor incididunt ut labore et dolore magna aliquis ipsum suspendisse ultrices gravida. Risus commodo viverra maecenas accumsan lacus vel facilisis. Lorem ipsum dolor sit amet, consectetur adipiscing elit, sed do eiusmod tempor incididunt ut labore et dolore magna aliquaus ipsum suspendisse ultrices gus coenas accumsan lacus vel facilisis.</p>
<div class="abs btn" style="left:642px;top:2921px;width:160px">READ MORE <span class="btn-dot"><svg viewBox="0 0 14 14"><path d="M4 2l6 5-6 5" fill="none" stroke="#503c87" stroke-width="2.4"/></svg></span></div>

<!-- footer -->
<footer class="abs footer"></footer>
<div class="abs foot-brand"><div class="brand-dot"></div><div class="brand-name" style="font-size:23px">Harbourline Ventures Group</div></div>
<div class="abs social" style="left:208px"></div>
<div class="abs social" style="left:256px"></div>
<div class="abs social" style="left:305px"></div>
<div class="abs social" style="left:353px"></div>

<h4 class="abs foot-h" style="left:543px;top:3210px">Contact Info</h4>
<svg class="abs" style="left:543px;top:3271px" width="12" height="16" viewBox="0 0 12 16"><path d="M6 0a6 6 0 0 0-6 6c0 4.5 6 10 6 10s6-5.5 6-10a6 6 0 0 0-6-6zm0 8.5A2.5 2.5 0 1 1 6 3.5a2.5 2.5 0 0 1 0 5z" fill="#fff"/></svg>
<p class="abs foot-t" style="left:567px;top:3267px;width:180px">23,eius modi tempora incidu nt utlaboreet oluptat</p>
<svg class="abs" style="left:543px;top:3336px" width="14" height="14" viewBox="0 0 14 14"><path d="M3 1c.6-.6 1.5-.6 1.9 0l1.3 1.9c.3.6 0 1.3-.6 1.6-.3.2-.3.6 0 1.2l1.6 1.9c.4.4 1 .4 1.3.1.4-.6 1.3-.8 1.7-.3l1.5 1.5c.5.5.4 1.3-.2 1.7C9.6 14 6.8 12.8 4.5 10.2S1.4 3 3 1z" fill="#fff"/></svg>
<p class="abs foot-t" style="left:567px;top:3332px">Phone : +1 555 014 2290</p>

<h4 class="abs foot-h" style="left:825px;top:3210px">Quick Links</h4>
<p class="abs foot-t" style="left:825px;top:3269px;line-height:28px">Home<br>Businesses for Sale<br>What we do<br>Our people</p>
<p class="abs foot-t" style="left:967px;top:3269px;line-height:28px">Industries<br>Blog<br>Confidentiality<br>Contact</p>

<div class="abs legal">© 2022 Harbourline Ventures Group. All rights reserved &nbsp;|&nbsp; Privacy &nbsp;|&nbsp; Terms of Use</div>

</body>
</html>
```